Brisk Fixworks business card

I need business card for my business, I think you have all my details.six months ago I design with you car wrap design. We would like to design both side of the card. On front of card we would like logo , Name and our contact details.
At the back we are looking to mentioned our services.
The name will be:
Gulbadin Norzai
Managing Director
Ph:07955384217
Email:info@brisk-fixworks.com
Web:www.brisk-fixworks.com
So we have our logo, you don’t need to change the logo.
Please see the attachment.
Thanks

Target Market(s)

Home improvement

Industry/Entity Type

Home Improvement

Contact Information for Business Card

Company name: Brisk Fixworks
Name: Gulbadin Norzai
Position: Director
Ph:07955384217
Web: www.brisk-fixworks.com
Add: 14 Garwick Lane
Carrowby
TW3 9QL
SECOND PERSON
Nasrullah norzai
Position: Handyman
Ph: 07822 643157
Email: info@brisk-fixworks.com
Add: 62 Bramcote Vale Drive
Carrowby
TW7 2KD

```html
<!DOCTYPE html>
<html lang="en">
<head>
<meta charset="utf-8">
<title>Brisk Fixworks business card</title>
<link rel="stylesheet" href="https://fonts.googleapis.com/css2?family=Michroma&family=Arimo:wght@400&display=swap">
<style>
  :root {
    --stage: #2b2b2d;
    --paper: #ffffff;
    --navy: #253a8c;
    --red: #e11f30;
    --ink: #3a3a3a;
    --gold: #f2a81d;
  }
  html, body { margin: 0; padding: 0; overflow: hidden; }
  .canvas {
    position: relative;
    width: 1200px; height: 1015px;
    background: var(--stage);
    overflow: hidden;
  }
  .card {
    position: absolute;
    width: 780px; height: 446px;
    background: var(--paper);
    box-shadow: 0 10px 30px rgba(0,0,0,.45);
    overflow: hidden;
  }
  /* Services side */
  .card--services { left: 60px; top: 44px; }
  .services-grid {
    position: absolute; left: 22px; top: 22px; right: 22px; bottom: 18px;
    display: grid;
    grid-template-columns: repeat(5, 1fr);
    grid-template-rows: 1fr 1fr;
    column-gap: 0; row-gap: 16px;
  }
  .service { display: flex; flex-direction: column; }
  .service__photo { flex: 1; }
  .service__label {
    font-family: "Arimo", Arial, sans-serif;
    font-size: 15px; letter-spacing: 1px;
    color: var(--navy);
    text-align: center;
    padding-top: 8px; height: 22px;
  }
  /* Contact side */
  .card--contact { left: 360px; top: 540px; }
  .brand-panel {
    position: absolute; left: 0; top: 0; width: 400px; height: 100%;
    background: var(--red);
  }
  .brand-frame {
    position: absolute; left: 28px; top: 30px; width: 320px; height: 370px;
    background: var(--paper);
    border: 12px solid var(--navy);
    border-radius: 0 0 160px 160px;
    box-sizing: border-box;
    display: flex; align-items: center; justify-content: center; gap: 12px;
  }
  .brand-name {
    font-family: "Michroma", sans-serif;
    font-size: 20px; color: var(--navy);
  }
  .brand-mark { width: 16px; height: 16px; background: var(--navy); }
  .accent-band {
    position: absolute; right: 0; bottom: 0; width: 330px; height: 34px;
    background: var(--navy);
  }
  .accent-band::before {
    content: ""; position: absolute; left: -120px; top: 0; width: 120px; height: 34px;
    background: var(--red);
  }
  .contact {
    position: absolute; left: 420px; top: 70px; width: 340px;
    font-family: "Michroma", sans-serif; color: var(--ink);
  }
  .contact__name { margin: 0; font-size: 19px; color: var(--navy); letter-spacing: .5px; }
  .contact__role { margin: 4px 0 26px; font-size: 12px; color: var(--ink); }
  .contact__list { list-style: none; margin: 0; padding: 0; }
  .contact__item {
    display: flex; align-items: flex-start; gap: 10px;
    font-size: 12px; line-height: 17px; margin-bottom: 10px;
  }
  .contact__item svg { flex: none; width: 16px; height: 16px; }
  .contact__web-strong { color: var(--navy); }
</style>
</head>
<body>
<main class="canvas">

  <section class="card card--services" aria-label="Services side">
    <div class="services-grid">
      <div class="service"><div class="service__photo" role="img" aria-label="Photo of a plumber fixing a sink pipe" style="background:linear-gradient(135deg,#d9dcdf,#9aa0a6)"></div><div class="service__label">PLUMBING</div></div>
      <div class="service"><div class="service__photo" role="img" aria-label="Photo of hands planing wood" style="background:linear-gradient(135deg,#7a5a3c,#c7a27a)"></div><div class="service__label">CARPENTRY</div></div>
      <div class="service"><div class="service__photo" role="img" aria-label="Photo of a paint roller on a wall" style="background:linear-gradient(135deg,#f1f1f1,#8fd0e8)"></div><div class="service__label">PAINTING</div></div>
      <div class="service"><div class="service__photo" role="img" aria-label="Photo of turf being laid" style="background:linear-gradient(180deg,#8a7a5e,#4f9a2c)"></div><div class="service__label">GARDENING</div></div>
      <div class="service"><div class="service__photo" role="img" aria-label="Photo of timber decking boards" style="background:linear-gradient(135deg,#e7d8bf,#b69a73)"></div><div class="service__label">DECKING</div></div>
      <div class="service"><div class="service__photo" role="img" aria-label="Photo of a worker drilling a fence panel" style="background:linear-gradient(135deg,#d7bd62,#e8862a)"></div><div class="service__label">FENCE</div></div>
      <div class="service"><div class="service__photo" role="img" aria-label="Photo of a gloved hand cleaning a gutter" style="background:linear-gradient(135deg,#3a3a3a,#b08060)"></div><div class="service__label">GUTTER</div></div>
      <div class="service"><div class="service__photo" role="img" aria-label="Photo of a trowel plastering a wall" style="background:linear-gradient(135deg,#b3a67e,#8e6f4a)"></div><div class="service__label">PLASTERING</div></div>
      <div class="service"><div class="service__photo" role="img" aria-label="Photo of white tiles being laid" style="background:linear-gradient(135deg,#e9e9e9,#c9c4bf)"></div><div class="service__label">TILLING</div></div>
      <div class="service"><div class="service__photo" role="img" aria-label="Photo of hands fitting a floor plank" style="background:linear-gradient(135deg,#e2e2e2,#8b5a3c)"></div><div class="service__label">FLOORING</div></div>
    </div>
  </section>

  <section class="card card--contact" aria-label="Contact side">
    <div class="brand-panel">
      <div class="brand-frame">
        <span class="brand-name">Brisk Fixworks</span>
        <span class="brand-mark"></span>
      </div>
    </div>
    <div class="accent-band"></div>

    <div class="contact">
      <h1 class="contact__name">GULBADIN NORZAI</h1>
      <p class="contact__role">DIRECTOR</p>
      <ul class="contact__list">
        <li class="contact__item">
          <svg viewBox="0 0 16 16" aria-hidden="true"><path fill="var(--gold)" d="M3.5 1.5l2.5 0 1 3.5-1.7 1.2a9 9 0 0 0 4.5 4.5l1.2-1.7 3.5 1v2.5a1.5 1.5 0 0 1-1.6 1.5A12.5 12.5 0 0 1 2 3.1 1.5 1.5 0 0 1 3.5 1.5z"/></svg>
          <span>07955384217</span>
        </li>
        <li class="contact__item">
          <svg viewBox="0 0 16 16" aria-hidden="true"><rect x="1" y="3" width="14" height="10" fill="var(--gold)"/><path d="M1 3l7 6 7-6" fill="none" stroke="#fff" stroke-width="1.4"/></svg>
          <span>INFO@BRISK-FIXWORKS.COM</span>
        </li>
        <li class="contact__item">
          <svg viewBox="0 0 16 16" aria-hidden="true"><circle cx="8" cy="8" r="6.5" fill="none" stroke="var(--gold)" stroke-width="1.6"/><path d="M1.5 8h13M8 1.5c-3 3.5-3 9.5 0 13M8 1.5c3 3.5 3 9.5 0 13" fill="none" stroke="var(--gold)" stroke-width="1.2"/></svg>
          <span>WWW.<span class="contact__web-strong">BRISK-FIXWORKS</span>.COM</span>
        </li>
        <li class="contact__item">
          <svg viewBox="0 0 16 16" aria-hidden="true"><path fill="var(--gold)" d="M8 1a5 5 0 0 1 5 5c0 3.5-5 9-5 9S3 9.5 3 6a5 5 0 0 1 5-5z"/><circle cx="8" cy="6" r="1.8" fill="#fff"/></svg>
          <span>14 GARWICK LANE<br>CARROWBY.TW3 9QL</span>
        </li>
      </ul>
    </div>
  </section>

</main>
</body>
</html>
```